Design for an iOS and Android app managing shopping list

The app allows you to keep manage shopping lists, each shopping list being made of items to buy...
We need a design for the 3 screens of the app:
a) global view showing list of (shopping) list
b) form enabling to edit the name of a (shopping) list
c) detailed view listing the contents/items of a (shopping) list
d) 1 text page [not illustrated]
2 "alerts" items are also to be designed: confirm and error pop ups.
No specific guidelines, nor logo or whatever.
It will be a free app distributed on iOS and Androïd.
We just want to make it looking nice & very usable for end users.

```html
<!DOCTYPE html>
<html lang="en">
<head>
<meta charset="utf-8">
<title>Update list name – validation warning</title>
<link href="https://fonts.googleapis.com/css2?family=Roboto:wght@300;400;500;700&display=swap" rel="stylesheet">
<style>
  :root{
    --page-bg:#f3f3f3;
    --screen-bg:#cbcbcb;
    --brand-teal:#1a8aa8;
    --field-bg:#d9d9d9;
    --field-border:#b3b3b3;
    --field-text:#8d8d8d;
    --scrim:rgba(0,0,0,0.55);
    --alert-red:#e63312;
    --alert-body:#ffffff;
    --alert-text:#666666;
    --ok-green:#3aab1e;
    --white:#ffffff;
    --kb-bg:#d1d5db;
    --kb-key:#ebebeb;
    --kb-key-alt:#aeb3be;
    --kb-text:#000000;
  }
  *{box-sizing:border-box;margin:0;padding:0}
  html,body{width:1200px;height:2353px;overflow:hidden;background:var(--page-bg)}
  body{position:relative;font-family:"Roboto",Arial,sans-serif}

  .screen{
    position:absolute;left:0;top:108px;width:411px;height:732px;
    transform:scale(2.9197);transform-origin:0 0;
    background:var(--screen-bg);overflow:hidden;
  }
  .status-bar{position:absolute;left:0;top:0;width:100%;height:30px;background:var(--brand-teal);color:var(--white);font-size:13px;font-weight:300}
  .status-bar .carrier{position:absolute;left:9px;top:8px;display:flex;align-items:center;gap:4px}
  .status-bar .time{position:absolute;left:0;right:0;top:8px;text-align:center}
  .status-bar .right{position:absolute;right:8px;top:8px;display:flex;align-items:center;gap:6px}

  .app-header{position:absolute;left:0;top:30px;width:100%;height:59px;background:var(--brand-teal);color:var(--white)}
  .app-header .back{position:absolute;left:12px;top:20px}
  .app-header .title{position:absolute;left:0;right:0;top:17px;text-align:center;font-size:19px;font-weight:300}

  .name-field{position:absolute;left:34px;top:154px;width:343px;height:45px;background:var(--field-bg);border:1px solid var(--field-border);border-radius:2px;padding:0 12px;display:flex;align-items:center;font-size:16px;color:var(--field-text);font-weight:300}
  .save-button{position:absolute;left:34px;top:230px;width:343px;height:45px;background:var(--brand-teal);color:var(--white);font-size:17px;font-weight:300;text-align:center;padding-top:12px}

  .keyboard{position:absolute;left:0;top:453px;width:100%;height:279px;background:var(--kb-bg)}
  .kb-row{position:absolute;left:0;width:100%;height:46px;display:flex;justify-content:center;gap:6px}
  .key{width:35px;height:46px;background:var(--kb-key);border-radius:5px;box-shadow:0 1px 0 rgba(0,0,0,0.35);display:flex;align-items:center;justify-content:center;font-size:24px;font-weight:300;color:var(--kb-text)}
  .key.alt{background:var(--kb-key-alt)}
  .key.small{font-size:17px}
  .row1{top:17px}.row2{top:86px}.row3{top:155px}.row4{top:224px}
  .row3,.row4{justify-content:flex-start}
  .row3 .shift{margin-left:4px;width:46px;margin-right:15px}
  .row3 .delete{margin-left:16px;width:46px}
  .row4 .k123{margin-left:4px;width:46px}
  .row4 .globe{width:43px;margin-left:5px}
  .row4 .mic{width:39px;margin-left:-1px}
  .row4 .space{width:53px;margin-left:-1px}
  .row4 .at{width:46px;margin-left:2px}
  .row4 .dot{width:43px;margin-left:0}
  .row4 .return{width:95px;margin-left:2px}

  .scrim{position:absolute;inset:0;background:var(--scrim)}

  .alert{position:absolute;left:27px;top:260px;width:357px;height:186px;background:var(--alert-body)}
  .alert-head{height:48px;background:var(--alert-red);color:var(--white);display:flex;align-items:center;justify-content:center;gap:8px;font-size:18px}
  .alert-message{margin-top:15px;text-align:center;font-size:14.5px;line-height:24px;color:var(--alert-text);font-weight:400}
  .alert-ok{position:absolute;left:160px;top:133px;width:36px;height:36px;border-radius:50%;background:var(--ok-green);color:var(--white);font-size:13px;font-weight:700;display:flex;align-items:center;justify-content:center}
</style>
</head>
<body>
<main class="screen">
  <div class="status-bar">
    <div class="carrier">
      <svg width="36" height="7" viewBox="0 0 36 7"><g fill="#fff"><circle cx="3.5" cy="3.5" r="3"/><circle cx="10.5" cy="3.5" r="3"/><circle cx="17.5" cy="3.5" r="3"/></g><g fill="none" stroke="#fff" stroke-width="0.9"><circle cx="24.5" cy="3.5" r="2.6"/><circle cx="31.5" cy="3.5" r="2.6"/></g></svg>
      <span>NOVA</span>
      <svg width="14" height="10" viewBox="0 0 14 10"><path d="M7 9.5 1 3.5a8.5 8.5 0 0 1 12 0z" fill="#fff"/></svg>
    </div>
    <div class="time">4:21 PM</div>
    <div class="right">
      <svg width="8" height="13" viewBox="0 0 8 13"><path d="M1 3.5 7 9.5 4 12.5V.5l3 3-6 6" fill="none" stroke="#fff" stroke-width="1.1"/></svg>
      <span>100%</span>
      <svg width="26" height="11" viewBox="0 0 26 11"><rect x="0.5" y="0.5" width="22" height="10" rx="2" fill="none" stroke="#fff"/><rect x="2" y="2" width="19" height="7" rx="1" fill="#fff"/><rect x="23.5" y="3.5" width="2" height="4" fill="#fff"/></svg>
    </div>
  </div>

  <header class="app-header">
    <svg class="back" width="10" height="18" viewBox="0 0 10 18"><path d="M9 1 1 9l8 8" fill="none" stroke="#fff" stroke-width="1.5"/></svg>
    <h1 class="title" style="font-weight:300;font-size:19px">Update list Name</h1>
  </header>

  <div class="name-field">List Name</div>
  <div class="save-button">Save</div>

  <div class="keyboard">
    <div class="kb-row row1"><span class="key">Q</span><span class="key">W</span><span class="key">E</span><span class="key">R</span><span class="key">T</span><span class="key">Y</span><span class="key">U</span><span class="key">I</span><span class="key">O</span><span class="key">P</span></div>
    <div class="kb-row row2"><span class="key">A</span><span class="key">S</span><span class="key">D</span><span class="key">F</span><span class="key">G</span><span class="key">H</span><span class="key">J</span><span class="key">K</span><span class="key">L</span></div>
    <div class="kb-row row3">
      <span class="key alt shift"><svg width="20" height="18" viewBox="0 0 20 18"><path d="M10 1 1 10h5v7h8v-7h5z" fill="none" stroke="#000" stroke-width="1.2" stroke-linejoin="round"/></svg></span>
      <span class="key">Z</span><span class="key">X</span><span class="key">C</span><span class="key">V</span><span class="key">B</span><span class="key">N</span><span class="key">M</span>
      <span class="key alt delete"><svg width="26" height="18" viewBox="0 0 26 18"><path d="M8 1h16v16H8L1 9z" fill="none" stroke="#000" stroke-width="1.2" stroke-linejoin="round"/><path d="M12 5l8 8M20 5l-8 8" stroke="#000" stroke-width="1.2"/></svg></span>
    </div>
    <div class="kb-row row4">
      <span class="key alt small k123">123</span>
      <span class="key alt globe"><svg width="22" height="22" viewBox="0 0 22 22" fill="none" stroke="#000" stroke-width="1.1"><circle cx="11" cy="11" r="10"/><ellipse cx="11" cy="11" rx="4.5" ry="10"/><path d="M1 11h20M3 5.5h16M3 16.5h16M11 1v20"/></svg></span>
      <span class="key alt mic"><svg width="14" height="24" viewBox="0 0 14 24" fill="none" stroke="#000" stroke-width="1.2"><rect x="4" y="1" width="6" height="13" rx="3"/><path d="M1 10a6 6 0 0 0 12 0M7 16v6M3 22h8"/></svg></span>
      <span class="key small space">space</span>
      <span class="key alt at">@</span>
      <span class="key alt dot">.</span>
      <span class="key alt small return">return</span>
    </div>
  </div>

  <div class="scrim"></div>

  <section class="alert" role="alertdialog" aria-label="Warning">
    <div class="alert-head">
      <svg width="20" height="18" viewBox="0 0 20 18"><path d="M10 1.5 1 16.5h18z" fill="none" stroke="#fff" stroke-width="1.6" stroke-linejoin="round"/><path d="M10 6.5v5" stroke="#fff" stroke-width="1.6"/><circle cx="10" cy="13.8" r="1" fill="#fff"/></svg>
      <span>Warning</span>
    </div>
    <p class="alert-message">list name should at least 1 character<br>to be valid!</p>
    <div class="alert-ok">OK</div>
  </section>
</main>
</body>
</html>
```